QUORVIX - Sydney Based Technology Consultancy -Logo & Business Card design

Who are we?
-
Quorvix is an emerging and advanced technology consulting and professional services business based in Sydney, Australia. Quorvix specialising in increasing value to organisations through the effective use of current and emerging technologies, ensuring that technology is a sustainable catalyst to attaining stated business goals.

We pride ourselves in challenging the norm.

What do we want?
-
We are looking to update our "Brand" we already have a simple “home grown” logo and we are now looking for a new one, once we have this updated logo and businesses look and feel though the business card design we will refresh our website with the new logo and design thus updating the Companies overall look at feel.

Our current site is www.quorvix-example.net.au is a very basic wordpress site and we will be updating it once we have the new logo and designs done

Our initial thoughts on the new Quorvix identity are
• Logo Concept
- One of the key things is obviously the 8
- I was thinking that a logo that had 8 as the core of the logo would be cool,
- Almost like having a “ring” or hoop that is twisted to form an 8 with different services scribed on the inside.
- So we would have a Large 8 and the inside would have ring each service or section engraved.

• Brand / web Feel
- Simple
- Professional
- Innovative
- Clear
- Destination
- Unique
- Impartial
- Safe
- Leading edge
- Familiar

- Emerging technologies
- White and ice / glacier blue
- The familiar feel of the Brindle web site
- Embedded specialist Video clips

• Portfolio of Services
- Quorvix – A smart place for Smart people
- Quorvix – we provide the process to take ideas from awareness to reality
- Focus should be on the brand quality consistent clear local knowledge with regional, national, theatre and global presence

Access to Specialists
- Emerging technologies
- Sustainability
- Collaboration
- Data centre
- Virtualisation

• Adjacent ideas under the one Brand
- Tembrosk – Enable Business Collaboration
- Plinsk – Infrastructure Virtualisation
- morvo - smart people and processes
- skandel - Emerging technologies
- brunhavel - business to technology integration
- tolpin - Smart Infrastructure
- yusk – Connected communities
- dwol - sustainability

Target Market(s)

Australia, New Zealand and Asia pacific organisations that are typically English speaking.
Markets
- IT & Technology partners
- Banking and Finance
- Health

Industry/Entity Type

Business

Requirements
Must have
• Logo
Business cards
Colour pallette
3D Logo
Nice to have
• Style guide
Designer who can also assist with new Wordpress design
Should not have
• we don't want cheap looking, overtly flashy or gimmicky logo.

```html
<!DOCTYPE html>
<html lang="en">
<head>
<meta charset="utf-8">
<title>Quorvix Business Card</title>
<link href="https://fonts.googleapis.com/css2?family=Arimo:wght@400;700&display=swap" rel="stylesheet">
<style>
  :root {
    --backdrop: #1b1b1b;
    --card-white: #ffffff;
    --ice-blue: #27aae1;
    --text-grey: #8c8c8c;
    --title-grey: #7a7a7a;
  }
  html, body {
    margin: 0;
    width: 1200px;
    height: 900px;
    overflow: hidden;
    background: var(--backdrop);
    font-family: "Arimo", Arial, sans-serif;
  }
  .business-card {
    position: absolute;
    left: 60px;
    top: 143px;
    width: 1080px;
    height: 614px;
    background: var(--ice-blue);
    overflow: hidden;
  }
  .card-shape {
    position: absolute;
    inset: 0;
    width: 100%;
    height: 100%;
  }
  .card-shape path { fill: var(--card-white); }
  .brand-name {
    position: absolute;
    right: 64px;
    top: 32px;
    margin: 0;
    font-size: 116px;
    font-weight: 400;
    letter-spacing: 6px;
    color: var(--text-grey);
    line-height: 1;
    white-space: nowrap;
  }
  .brand-tagline {
    position: absolute;
    right: 73px;
    top: 148px;
    margin: 0;
    font-size: 19px;
    line-height: 1.2;
    color: var(--text-grey);
    letter-spacing: 0.9px;
    white-space: nowrap;
  }
  .person-name {
    position: absolute;
    left: 57px;
    top: 262px;
    margin: 0;
    font-size: 40px;
    font-weight: 700;
    color: var(--ice-blue);
  }
  .person-role {
    position: absolute;
    left: 57px;
    top: 312px;
    margin: 0;
    font-size: 29px;
    font-weight: 700;
    color: var(--title-grey);
  }
  .office-address {
    position: absolute;
    left: 57px;
    top: 352px;
    margin: 0;
    font-size: 29px;
    color: var(--text-grey);
    font-style: normal;
    white-space: nowrap;
  }
  .contact-row {
    position: absolute;
    display: flex;
    font-size: 29px;
    margin: 0;
    white-space: nowrap;
  }
  .contact-label { color: var(--ice-blue); width: 92px; }
  .contact-sep { color: var(--ice-blue); width: 38px; }
  .contact-value { color: var(--text-grey); }
  .row-email { left: 112px; top: 424px; }
  .row-tel { left: 152px; top: 461px; }
  .row-web { left: 196px; top: 498px; }
</style>
</head>
<body>
  <section class="business-card">
    <svg class="card-shape" viewBox="0 0 415 236" preserveAspectRatio="none" aria-hidden="true">
      <path d="M92 0 C35 18 4 70 4 125 C4 185 55 236 110 236 L318 236 C368 228 405 205 415 182 L415 8 L408 0 Z"/>
    </svg>

    <h1 class="brand-name">QUORVIX</h1>
    <p class="brand-tagline">Smart Technology Thinking, Delivering Real Results</p>

    <h2 class="person-name">Dalen Worsick</h2>
    <p class="person-role">Designer</p>
    <address class="office-address">Suite 41, 218 Harbour Ln, Sydney, NSW 2000 Australia</address>

    <p class="contact-row row-email"><span class="contact-label">email</span><span class="contact-sep">:</span><span class="contact-value">dalen@quorvix-example.net.au</span></p>
    <p class="contact-row row-tel"><span class="contact-label">tel</span><span class="contact-sep">:</span><span class="contact-value">+61-2-5550-0147</span></p>
    <p class="contact-row row-web"><span class="contact-label">web</span><span class="contact-sep">:</span><span class="contact-value">www.quorvix-example.net.au</span></p>
  </section>
</body>
</html>
```